Torvane Facilities Business Card Design

We would now like to design business cards with the new Torvane Facilities logo

Target Market(s)

Professional

Industry/Entity Type

Professional services

Contact Information for Business Card

Employee name, title, phone number, email address, corporate office address and logo.

Font styles to use
Sans Serif

Colors
0054AA
0677BA
7BADD7
CADEEF
E8F1F8

Requirements
Must have
• My logo
Should not have
• any other pictures or images besides my logo

```html
<!DOCTYPE html>
<html lang="en">
<head>
<meta charset="utf-8">
<title>Torvane Facilities Business Card</title>
<link href="https://fonts.googleapis.com/css2?family=Lato:wght@400;700;900&display=swap" rel="stylesheet">
<style>
  :root {
    --backdrop: #d4d4d4;
    --brand-deep: #3d6db5;
    --brand-mid: #4a80c4;
    --brand-light: #67a8d8;
    --ink-blue: #3a68b8;
    --paper: #ffffff;
    --wash: #eef0f7;
  }
  * { margin: 0; padding: 0; box-sizing: border-box; }
  html, body { width: 1200px; height: 800px; overflow: hidden; }
  body {
    background: var(--backdrop);
    font-family: "Lato", sans-serif;
    display: flex;
    align-items: center;
    justify-content: center;
    gap: 40px;
  }
  .card {
    width: 540px;
    height: 309px;
    position: relative;
    overflow: hidden;
    box-shadow: 0 6px 18px rgba(0,0,0,0.18);
  }
  /* Front */
  .card-front {
    background:
      radial-gradient(ellipse 60% 70% at 42% 48%, var(--brand-light) 0%, rgba(103,168,216,0) 70%),
      linear-gradient(135deg, var(--brand-deep) 0%, var(--brand-mid) 50%, var(--brand-deep) 100%);
    color: var(--paper);
  }
  .front-brand {
    position: absolute;
    left: 120px;
    top: 98px;
    display: flex;
    align-items: center;
    gap: 18px;
  }
  .brand-square {
    width: 64px;
    height: 64px;
    border: 8px solid currentColor;
  }
  .brand-name {
    font-weight: 900;
    font-size: 38px;
    line-height: 1.02;
    letter-spacing: 1px;
    text-transform: uppercase;
  }
  .front-web {
    position: absolute;
    left: 214px;
    top: 210px;
    font-size: 15px;
    letter-spacing: 0.3px;
  }
  /* Back */
  .card-back {
    background:
      linear-gradient(160deg, var(--paper) 55%, var(--wash) 100%);
    color: var(--ink-blue);
  }
  .back-brand {
    position: absolute;
    left: 30px;
    top: 36px;
    display: flex;
    align-items: center;
    gap: 10px;
  }
  .back-brand .brand-square {
    width: 32px;
    height: 32px;
    border-width: 5px;
  }
  .back-brand .brand-name {
    font-size: 19px;
  }
  .contact {
    position: absolute;
    left: 270px;
    top: 104px;
    font-size: 13px;
    line-height: 1.35;
  }
  .contact-name {
    font-weight: 900;
    font-size: 17px;
    text-transform: uppercase;
    letter-spacing: 0.4px;
  }
  .contact-title { margin-bottom: 14px; }
  .contact-address { margin-bottom: 14px; }
</style>
</head>
<body>
  <section class="card card-front">
    <div class="front-brand">
      <span class="brand-square"></span>
      <div class="brand-name">Torvane<br>Facilities</div>
    </div>
    <div class="front-web">www.torvanefacilities.com</div>
  </section>

  <section class="card card-back">
    <div class="back-brand">
      <span class="brand-square"></span>
      <div class="brand-name">Torvane<br>Facilities</div>
    </div>
    <div class="contact">
      <div class="contact-name">Dana Whitlow</div>
      <div class="contact-title">Vice President</div>
      <div class="contact-address">418 Harbor Ridge Rd Suite 4<br>Lakemont, NJ 08912</div>
      <div>P: 555-014-2200</div>
      <div>E: dana.whitlow@torvanefacilities.com</div>
      <div>W: www.torvanefacilities.com</div>
    </div>
  </section>
</body>
</html>
```